Christmas Candle Label

We require a Christmas candle label that fits with our current brand (see larkvalewickworks.example, and also example attached). On the attached we would like the word 'Tovane - Mirreld' replaced with 'Merry Christmas' (or something creative that you can come up with) and the writing on the left hand side 'lose yourself in the subtle.........' replaced with 'its beginning to smell a lot like Christmas' (or something creative that you can come up with). We would like the flora image in the background replaced with a line drawing of a Christmas tree or holy or anything else that is appropriate. Finally we are not sure if a different colour label i.e. red, maroon or green (with lots of black, silver or gold writing) instead of black would be best for this label. It may be best to see a comparison of our original black label with black, silver or gold writing, and the other colours.

```html
<!DOCTYPE html>
<html lang="en">
<head>
<meta charset="utf-8">
<title>Christmas Candle Label</title>
<link rel="stylesheet" href="https://fonts.googleapis.com/css2?family=Poppins:wght@300;400;500&display=swap">
<style>
  :root {
    --canvas: #ece8e2;
    --label-black: #1b1a1a;
    --ink-gold: #bcb0a0;
    --ink-gold-soft: #8f867a;
  }
  * { margin: 0; padding: 0; box-sizing: border-box; }
  html, body {
    width: 1200px; height: 1200px; overflow: hidden;
    background: var(--canvas);
  }
  .canvas { position: relative; width: 1200px; height: 1200px; }
  .label {
    position: absolute; left: 40px; top: 360px;
    width: 1120px; height: 481px;
    background: radial-gradient(ellipse at 50% 40%, #222120 0%, var(--label-black) 70%);
    color: var(--ink-gold);
    overflow: hidden;
  }
  .deco-hanging {
    position: absolute; top: 0;
    background: linear-gradient(180deg, rgba(74,70,64,0.15) 0%, rgba(74,70,64,0.55) 100%);
    border-radius: 0 0 40px 40px;
  }
  .deco-hanging.left { left: 131px; width: 108px; height: 251px; }
  .deco-hanging.right { left: 854px; width: 106px; height: 276px; }
  .tree-mark {
    position: absolute; left: 520px; top: 105px; width: 80px; height: 113px;
    background: linear-gradient(180deg, #a99d8e 0%, var(--ink-gold) 100%);
    opacity: 0.85;
    border-radius: 40px 40px 6px 6px;
  }
  .title-block {
    position: absolute; left: 380px; top: 228px; width: 360px;
    text-align: center;
  }
  .title-merry {
    display: block; height: 26px; line-height: 26px;
    font-family: "Poppins", sans-serif; font-weight: 400;
    font-size: 17px; letter-spacing: 4px; color: var(--ink-gold);
  }
  .title-main {
    font-family: "Poppins", sans-serif; font-weight: 300;
    font-size: 50px; line-height: 62px; letter-spacing: 1px;
    color: var(--ink-gold);
    margin-top: 4px;
  }
  .title-rule {
    width: 260px; height: 1px; margin: 20px auto 0;
    background: var(--ink-gold-soft);
  }
  .origin-line {
    position: absolute; left: 380px; top: 384px; width: 360px;
    text-align: center;
    font-family: "Poppins", sans-serif; font-weight: 500;
    font-size: 10.5px; letter-spacing: 2.2px; color: var(--ink-gold-soft);
  }
  .tagline {
    position: absolute; left: 61px; top: 252px;
    font-family: "Poppins", sans-serif; font-weight: 300;
    font-size: 23px; line-height: 33px; letter-spacing: -0.4px;
    color: var(--ink-gold);
  }
  .product-details {
    position: absolute; right: 54px; top: 234px;
    text-align: right;
    font-family: "Poppins", sans-serif; font-weight: 300;
    font-size: 15px; line-height: 19px; letter-spacing: -0.3px;
    color: var(--ink-gold);
  }
  .product-details p + p { margin-top: 8px; }
  .product-details .detail-gap { margin-top: 21px; }
</style>
</head>
<body>
<div class="canvas">
  <section class="label">
    <div class="deco-hanging left" role="img" aria-label="Hanging baubles, stars and snowflakes on fine strings"></div>
    <div class="deco-hanging right" role="img" aria-label="Hanging baubles, stars and snowflakes on fine strings"></div>

    <div class="tree-mark" role="img" aria-label="Christmas tree with star on top"></div>

    <div class="title-block">
      <span class="title-merry">MERRY</span>
      <h1 class="title-main">CHRISTMAS</h1>
      <div class="title-rule"></div>
    </div>

    <p class="origin-line">Handcrafted in Southern Tasmania</p>

    <p class="tagline">its<br>beginning<br>to smell<br>a lot like<br>Christmas</p>

    <div class="product-details">
      <p>500g<br>90+ hour</p>
      <p>Hand poured,<br>scented soy and<br>coconut candle</p>
      <p class="detail-gap">Made with all<br>natural ingredients</p>
    </div>
  </section>
</div>
</body>
</html>
```